New Website - vantomix.com

This is what we looking for - http://www.sketchpoolery.com/design/738412
Updates

hello, im back and i want some good designs for my website.. i need really creative ideas. this is for a cellphone provider company. Vantomix mobile please provide me a good ideas and i will go with u also to program the website

Font styles to use
Sans Serif

```html
<!DOCTYPE html>
<html lang="en">
<head>
<meta charset="utf-8">
<title>Vantomix Communications</title>
<link href="https://fonts.googleapis.com/css2?family=Open+Sans:wght@400;600&display=swap" rel="stylesheet">
<style>
:root{
  --blue:#2b8fd8;
  --blue-light:#6cc0f2;
  --blue-dark:#3aa0e6;
  --ink:#3a3a3a;
  --muted:#555;
  --rule:#e3e3e3;
  --btn:#3d3d3d;
  --footer:#ececec;
  --red:#a01c1c;
}
*{box-sizing:border-box;margin:0;padding:0}
html,body{width:1104px;height:1200px;overflow:hidden;background:#fff}
body{font-family:"Open Sans",Arial,sans-serif;color:var(--ink);position:relative}
.header{position:absolute;left:0;top:0;width:1104px;height:84px}
.brand{position:absolute;left:92px;top:18px;display:flex;align-items:center;gap:12px}
.brand-dot{width:34px;height:34px;border-radius:50%;background:var(--blue)}
.brand-name{font-size:36px;font-weight:600;color:#222;letter-spacing:.5px}
.search{position:absolute;left:850px;top:27px;width:163px;height:29px;border:1px solid #d6d6d6;border-radius:2px;font-size:12px;color:#999;padding:8px 0 0 11px}
.search svg{position:absolute;right:4px;top:4px}
.search::after{content:"";position:absolute;right:28px;top:4px;height:19px;border-left:1px solid #ddd}
.nav{position:absolute;left:0;top:84px;width:1104px;height:46px;background:linear-gradient(#7ccbf6,#47aaec)}
.nav ul{list-style:none;position:absolute;left:93px;top:0;display:flex;height:46px}
.nav li{color:#fff;font-size:14px;font-weight:600;padding:0 22px;line-height:46px;border-right:1px solid rgba(255,255,255,.35)}
.nav li.active{background:#2e2e2e;padding:0 20px}
.hero{position:absolute;left:91px;top:142px;width:922px;height:356px;background:linear-gradient(90deg,#f2f3f5 0%,#e4e7ea 45%,#c9d4df 60%,#e7eef5 100%)}
.hero-photo{position:absolute;right:0;top:0;width:400px;height:356px;background:linear-gradient(160deg,#d8b07a 0%,#e9d2b8 40%,#1d2a4a 80%,#15203a 100%)}
.hero-text{position:absolute;left:24px;top:106px;width:380px;font-size:20px;line-height:27px;color:#333}
.hero-btn{position:absolute;left:24px;top:193px;width:162px;height:39px;background:linear-gradient(#58b4ee,#3a98de);color:#fff;font-size:17px;font-weight:600;line-height:39px;text-align:center;border-radius:2px}
.dots{position:absolute;left:27px;top:318px;display:flex;gap:8px}
.dots span{width:13px;height:13px;border-radius:50%;background:#8a8a8a;box-shadow:inset 0 1px 2px rgba(0,0,0,.4)}
.dots span.on{background:#333}
.welcome{position:absolute;left:93px;top:524px;width:670px}
.welcome h1{font-size:25px;font-weight:400;color:var(--blue);margin-bottom:10px}
.welcome p{font-size:12.5px;line-height:21px;color:var(--muted)}
.video{position:absolute;left:784px;top:539px;width:229px;height:143px;background:linear-gradient(135deg,#3c4046,#1c1e22);border-radius:2px}
.play{position:absolute;left:50%;top:50%;transform:translate(-50%,-50%)}
.divider{position:absolute;left:92px;top:711px;width:921px;border-top:1px solid var(--rule)}
.col{position:absolute;top:733px;width:300px}
.col h2{font-size:25px;font-weight:400;color:var(--blue);line-height:30px}
.col h3{font-size:13.5px;font-weight:600;color:#333;letter-spacing:.2px;margin-top:0}
.col .pic{position:relative;width:288px;height:134px;margin-top:10px}
.col ul{list-style:none;margin-top:14px}
.col li{position:relative;font-size:13px;color:var(--muted);padding-left:22px;line-height:25px}
.col li svg{position:absolute;left:2px;top:7px}
.col li.feature{color:var(--red)}
.col li.wrap{line-height:16px;padding-top:5px}
.col li.wrap svg{top:9px}
.col .btn{position:absolute;top:326px;left:0;height:29px;padding:0 12px;background:var(--btn);color:#fff;font-size:13px;line-height:29px}
.check-row{display:flex;gap:6px;padding-left:22px;margin:2px 0 4px}
.check-row span{height:26px;background:#eee;border:1px solid #ddd;border-radius:2px}
.check-row b{height:26px;width:48px;background:var(--btn);color:#fff;font-weight:400;font-size:12px;line-height:26px;text-align:center;border-radius:2px}
.footer{position:absolute;left:0;top:1116px;width:1104px;height:84px;background:var(--footer)}
.footer nav{position:absolute;left:92px;top:20px;font-size:12px;color:#555;word-spacing:1px}
.footer nav span{margin:0 8px;color:#777}
.footer p{position:absolute;left:92px;top:47px;font-size:12px;color:#555}
.social{position:absolute;left:962px;top:32px;display:flex;gap:4px}
.social span{width:22px;height:22px;border-radius:2px}
.social .s1{background:#3b5a99}
.social .s2{background:#4cb3e6}
</style>
</head>
<body>
<header class="header">
  <div class="brand"><span class="brand-dot"></span><span class="brand-name">Vantomix</span></div>
  <div class="search">Search
    <svg width="20" height="20" viewBox="0 0 20 20"><circle cx="8" cy="8" r="5.5" fill="none" stroke="#888" stroke-width="2"/><path d="M12 12l5 5" stroke="#888" stroke-width="2.5" stroke-linecap="round"/></svg>
  </div>
</header>

<nav class="nav">
  <ul>
    <li class="active">HOME</li><li>ABOUT US</li><li>SERVICES</li><li>PRODUCTS</li><li>FAQ</li><li>PARTNERS</li><li>CONTACT US</li><li>REQUEST A QUOTE</li>
  </ul>
</nav>

<section class="hero">
  <div class="hero-photo" role="img" aria-label="Smiling support agent wearing a headset in an office"></div>
  <p class="hero-text">A revolutionary digital phone service that will save you, your family, and your business lots of money.</p>
  <div class="hero-btn">Get Started Now</div>
  <div class="dots"><span class="on"></span><span></span><span></span><span></span></div>
</section>

<section class="welcome">
  <h1>Welcome to Vantomix</h1>
  <p>Donec tincidunt consectetur nibh nec egestas. Donec placerat nulla lacus. Pellentesque habitant morbi tristique senectus et netus et malesuada fames ac turpis egestas. Duis pharetra lorem consequat fringilla porttitor. Curabitur in tellus ac quam blandit tristique. Aliquam erat volutpat. Nullam placerat orci eu pretium tincidunt. Curabitur sit amet venenatis est, sed volutpat turpis. Nunc tincidunt quis erat sit amet viverra. Nulla tincidunt libero augue, eu congue est fermentum id. Vivamus gravida erat sed diam vehicula, id euismod magna convallis. Vestibulum congue lectus massa, at eleifend velit mattis imperdiet.</p>
</section>
<div class="video" role="img" aria-label="Video still of a businessman holding a tablet in a server room">
  <svg class="play" width="58" height="58" viewBox="0 0 58 58"><circle cx="29" cy="29" r="26" fill="rgba(0,0,0,.25)" stroke="#fff" stroke-width="4"/><path d="M23 17l17 12-17 12z" fill="#fff"/></svg>
</div>

<div class="divider"></div>

<section class="col" style="left:94px">
  <h2>Affordable</h2>
  <h3>START SAVING TODAY!</h3>
  <div class="pic" role="img" aria-label="Hand dialing a black desk telephone" style="background:linear-gradient(135deg,#e8e8e8,#bfc3c7 50%,#2a2a2a 70%,#d9d9d9)"></div>
  <ul>
    <li><svg width="12" height="12" viewBox="0 0 12 12"><circle cx="6" cy="6" r="5" fill="none" stroke="#2b8fd8" stroke-width="1.6"/><path d="M4 6h4M6 4l2 2-2 2" fill="none" stroke="#2b8fd8" stroke-width="1.5"/></svg>Unlimited local and long distance calling</li>
    <li><svg width="12" height="12" viewBox="0 0 12 12"><circle cx="6" cy="6" r="5" fill="none" stroke="#2b8fd8" stroke-width="1.6"/><path d="M4 6h4M6 4l2 2-2 2" fill="none" stroke="#2b8fd8" stroke-width="1.5"/></svg>5 nation unlimited international</li>
    <li><svg width="12" height="12" viewBox="0 0 12 12"><circle cx="6" cy="6" r="5" fill="none" stroke="#2b8fd8" stroke-width="1.6"/><path d="M4 6h4M6 4l2 2-2 2" fill="none" stroke="#2b8fd8" stroke-width="1.5"/></svg>No set-up, equipment fees, or hidden charges</li>
    <li><svg width="12" height="12" viewBox="0 0 12 12"><circle cx="6" cy="6" r="5" fill="none" stroke="#2b8fd8" stroke-width="1.6"/><path d="M4 6h4M6 4l2 2-2 2" fill="none" stroke="#2b8fd8" stroke-width="1.5"/></svg>No contracts or commitments</li>
  </ul>
  <div class="btn">COMPARE RATE AND PLANS</div>
</section>

<section class="col" style="left:409px">
  <h2>Powerful</h2>
  <h3>INCREDIBLE FEATURES, STANDARD</h3>
  <div class="pic" role="img" aria-label="Video still of a glowing network of connected people icons" style="background:radial-gradient(circle at 45% 50%,#8a8f7a,#3e4a52 60%,#2b3138)">
    <svg class="play" width="62" height="62" viewBox="0 0 62 62"><circle cx="31" cy="31" r="28" fill="rgba(0,0,0,.2)" stroke="#fff" stroke-width="4"/><path d="M25 18l18 13-18 13z" fill="#fff"/></svg>
  </div>
  <ul>
    <li><svg width="12" height="12" viewBox="0 0 12 12"><circle cx="6" cy="6" r="5" fill="none" stroke="#2b8fd8" stroke-width="1.6"/><path d="M4 6h4M6 4l2 2-2 2" fill="none" stroke="#2b8fd8" stroke-width="1.5"/></svg>Seamless integration with Mailvane</li>
    <li><svg width="12" height="12" viewBox="0 0 12 12"><circle cx="6" cy="6" r="5" fill="none" stroke="#2b8fd8" stroke-width="1.6"/><path d="M4 6h4M6 4l2 2-2 2" fill="none" stroke="#2b8fd8" stroke-width="1.5"/></svg>Get calls and voicemail anywhere</li>
    <li><svg width="12" height="12" viewBox="0 0 12 12"><circle cx="6" cy="6" r="5" fill="none" stroke="#2b8fd8" stroke-width="1.6"/><path d="M4 6h4M6 4l2 2-2 2" fill="none" stroke="#2b8fd8" stroke-width="1.5"/></svg>100% hurrican proof</li>
    <li class="feature"><svg width="12" height="12" viewBox="0 0 12 12"><circle cx="6" cy="6" r="5" fill="none" stroke="#2b8fd8" stroke-width="1.6"/><path d="M4 6h4M6 4l2 2-2 2" fill="none" stroke="#2b8fd8" stroke-width="1.5"/></svg>Featuring the Power of Callverra!</li>
  </ul>
  <div class="btn">TAKE THE TOUR</div>
</section>

<section class="col" style="left:724px">
  <h2>Flexible</h2>
  <h3>SERVICE ON YOUR OWN TERMS</h3>
  <div class="pic" role="img" aria-label="Businesswoman on a phone call holding a tablet in a bright lobby" style="background:linear-gradient(90deg,#d9dde2,#c4c8cc 45%,#2a2c33 70%,#e6e6e6)"></div>
  <ul>
    <li><svg width="12" height="12" viewBox="0 0 12 12"><circle cx="6" cy="6" r="5" fill="none" stroke="#2b8fd8" stroke-width="1.6"/><path d="M4 6h4M6 4l2 2-2 2" fill="none" stroke="#2b8fd8" stroke-width="1.5"/></svg>Keep your Number!</li>
  </ul>
  <div class="check-row"><span style="width:58px"></span><span style="width:59px"></span><span style="width:80px"></span><b>Check</b></div>
  <ul style="margin-top:0">
    <li><svg width="12" height="12" viewBox="0 0 12 12"><circle cx="6" cy="6" r="5" fill="none" stroke="#2b8fd8" stroke-width="1.6"/><path d="M4 6h4M6 4l2 2-2 2" fill="none" stroke="#2b8fd8" stroke-width="1.5"/></svg>Choose your own area code</li>
    <li class="wrap"><svg width="12" height="12" viewBox="0 0 12 12"><circle cx="6" cy="6" r="5" fill="none" stroke="#2b8fd8" stroke-width="1.6"/><path d="M4 6h4M6 4l2 2-2 2" fill="none" stroke="#2b8fd8" stroke-width="1.5"/></svg>Custom-tailored business solutions, both hosted local</li>
  </ul>
  <div class="btn">LEARN HOW IT WORKS</div>
</section>

<footer class="footer">
  <nav>Home<span>|</span>About us<span>|</span>Services<span>|</span>Products<span>|</span>FAQ<span>|</span>Partners<span>|</span>Contact us<span>|</span>Request a Quote</nav>
  <p>Copyright © 2014 Vantomix Communications. All rights reserved</p>
  <div class="social"><span class="s1"></span><span class="s2"></span></div>
</footer>
</body>
</html>
```